professional looking data specialist website

I've recently had a new logo designed and I'm now looking to get a professional looking website built. This is for a new company that specialises in data. We look to support companies with business intelligence, report modelling, data governance to new european legislation (GDPR). We are offer consultancy or we can attend site and complete work when required. Our target arket is united kingdom wide and we are specifically aiming at small to medium sized companies.

Target Market(s)

small to medium enterprise companies from all industries

Industry/Entity Type

Professional Service

Coding

Coded - Design and coding required

Number of Pages Required

4 page

Font styles to use
Sans Serif

Colors

Designer to choose colors to be used in the design.

Requirements
Must have
• Professional look including the company logo, need to have ability to request more information from us so needs a inquiries page, seperate pages for the different offerings, data governance, report modelling, business intelligence implementation, data protection
Nice to have
• any website interaction, animation, etc
Should not have
• too many colours, too busy pages, must look professional

```html
<!DOCTYPE html>
<html lang="en">
<head>
<meta charset="utf-8">
<title>Northvale Ltd — Data Specialists</title>
<link rel="stylesheet" href="https://fonts.googleapis.com/css2?family=Josefin+Sans:wght@600;700&family=Lato:wght@400;700&display=swap">
<style>
:root{
  --blue:#0f6fbf;
  --blue-band:rgba(47,134,205,.88);
  --navy:#14234a;
  --ink:#2b2b2b;
  --text:#666;
  --field:#efefef;
  --field-line:#d9d9d9;
  --label:#d4d4d4;
  --white:#fff;
}
*{margin:0;padding:0;box-sizing:border-box}
html,body{width:778px;height:1200px;overflow:hidden;background:var(--white)}
body{position:relative;font-family:'Lato',sans-serif;color:var(--ink)}
.abs{position:absolute}

.hero{left:0;top:0;width:778px;height:440px;
  background:linear-gradient(180deg,#eef2f6 0%,#dfe6ee 45%,#c9d3de 75%,#b7c3cf 100%)}
.brand{left:50px;top:30px;display:flex;align-items:center;gap:8px}
.brand-mark{width:22px;height:22px;background:var(--blue)}
.brand-name{font-family:'Lato',sans-serif;font-weight:700;font-size:22px;color:var(--blue)}
.nav{top:28px;left:410px;display:flex;font-size:12px;letter-spacing:.3px}
.nav a{color:#333;text-decoration:none;height:28px;line-height:26px;border:1.5px solid transparent}
.nav .home{width:62px;text-align:center;color:var(--blue);border-color:var(--blue)}
.nav .about{margin-left:27px}
.nav .services{margin-left:45px}
.nav .contact{margin-left:43px}

.slide-band{left:0;top:372px;width:778px;height:67px;background:var(--blue-band);color:var(--white)}
.slide-title{left:52px;top:12px;font-family:'Josefin Sans',sans-serif;font-weight:700;font-size:21px;letter-spacing:.4px}
.slide-text{left:51px;top:38px;font-size:12px}
.arrow{top:22px;width:27px;height:27px;border:1.5px solid var(--white);display:flex;align-items:center;justify-content:center;font-size:20px;line-height:1}
.arrow.prev{left:667px}
.arrow.next{left:701px}

.section-title{left:0;width:778px;text-align:center;font-family:'Josefin Sans',sans-serif;font-weight:700;font-size:26px;color:var(--blue);letter-spacing:.5px}
.about-title{top:478px}
.about-text{left:106px;top:520px;width:566px;text-align:center;font-size:11px;line-height:17.6px;color:var(--text)}

.card{top:622px;width:159px;height:206px}
.card .photo{position:absolute;left:0;top:0;width:159px;height:158px;border-top:3px solid var(--navy)}
.card .label{position:absolute;left:0;top:158px;width:159px;height:48px;background:var(--label);border-bottom:2px solid #333;
  display:flex;align-items:center;justify-content:center;text-align:center;font-family:'Josefin Sans',sans-serif;font-weight:700;font-size:11px;letter-spacing:.3px;color:#222;line-height:13px}
.card.active .photo{border-top-color:var(--blue)}
.card.active .label{border-bottom-color:var(--blue)}
.c1{left:50px}.c2{left:221px}.c3{left:392px}.c4{left:570px}
.c1 .photo{background:radial-gradient(circle at 45% 50%,#4a7fb5 0%,#1d3560 45%,#0c1530 100%)}
.c2 .photo{background:linear-gradient(180deg,#e9eef4 0%,#d7e0ea 60%,#c6d2de 100%)}
.c3 .photo{background:linear-gradient(120deg,#dfe3e8 0%,#b9c2cc 50%,#8f6b5a 100%)}
.c4 .photo{background:linear-gradient(160deg,#8a6d52 0%,#4f5a66 45%,#2c3540 100%)}
.read-more{left:35px;top:69px;width:89px;height:28px;border:1.5px solid #333;background:rgba(255,255,255,.85);
  font-size:12px;font-weight:700;display:flex;align-items:center;justify-content:center;color:#111}

.contact-title{top:866px}
.field{background:var(--field);border:1px solid var(--field-line);font-size:9px;color:#aaa;padding:4px 6px}
.f-name{left:138px;top:910px;width:246px;height:20px}
.f-email{left:388px;top:910px;width:246px;height:20px}
.f-message{left:138px;top:934px;width:425px;height:67px}
.send{left:566px;top:934px;width:68px;height:67px;border:1.5px solid var(--blue);color:var(--blue);
  display:flex;flex-direction:column;align-items:center;justify-content:center;gap:3px;font-size:14px;font-weight:700}

.footer-mark{left:375px;top:1034px;width:28px;height:28px;background:var(--blue);border:4px solid var(--white);outline:1px solid #cfd8e3}
.footer{left:0;top:1061px;width:778px;height:139px;background:var(--blue);color:var(--white)}
.f-item{top:52px;display:flex;align-items:center;gap:9px;font-size:9.5px;line-height:12px}
.f-icon{width:28px;height:28px;border-radius:50%;background:var(--white);display:flex;align-items:center;justify-content:center;flex:none}
.fi-1{left:49px;top:46px}.fi-2{left:242px}.fi-3{left:397px}.fi-4{left:556px}
.f-co{font-family:'Josefin Sans',sans-serif;font-weight:700;font-size:13px;line-height:16px}
.f-item b{font-weight:700}
.rule{left:36px;top:101px;width:706px;height:1px;background:rgba(255,255,255,.35)}
.copyright{left:0;top:115px;width:778px;text-align:center;font-size:9.5px}
.copyright b{font-family:'Josefin Sans',sans-serif;font-size:12px}
</style>
</head>
<body>

<div class="hero abs" role="img" aria-label="Smiling team of business people in a bright office with a growth chart behind them"></div>

<div class="brand abs"><span class="brand-mark"></span><span class="brand-name">Northvale Ltd</span></div>

<nav class="nav abs">
  <a class="home" href="#">HOME</a>
  <a class="about" href="#">ABOUT</a>
  <a class="services" href="#">SERVICES</a>
  <a class="contact" href="#">CONTACT</a>
</nav>

<div class="slide-band abs">
  <div class="slide-title abs">WE ARE SPECIALISES IN DATA</div>
  <div class="slide-text abs">Lorem Ipsum is simply dummy text of the printing and typesetting industry has been the industry.</div>
  <div class="arrow prev abs">«</div>
  <div class="arrow next abs">»</div>
</div>

<h2 class="section-title about-title abs">ABOUT NORTHVALE LTD.</h2>
<p class="about-text abs">Lorem Ipsum is simply dummy text of the printing and typesetting industry. Lorem Ipsum has been the industry's standard dummy text ever since the 1500s, when an unknown printer took a galley of type and scrambled it to make a type specimen book when an unknown printer took a galley of type and scrambled it to make a type specimen book printer took a galley of type and scrambled.</p>

<div class="card c1 abs">
  <div class="photo" role="img" aria-label="Hand holding glowing blue data cubes"></div>
  <div class="label">DATA GOVERNANCE</div>
</div>
<div class="card c2 active abs">
  <div class="photo" role="img" aria-label="Business person facing a wall of report charts"></div>
  <div class="read-more abs">Read More</div>
  <div class="label">REPORT MODELLING</div>
</div>
<div class="card c3 abs">
  <div class="photo" role="img" aria-label="Analysts working at computer screens"></div>
  <div class="label">BUSINESS INTELLIGENCE<br>IMPLEMENTION</div>
</div>
<div class="card c4 abs">
  <div class="photo" role="img" aria-label="Laptop with a security padlock on screen"></div>
  <div class="label">DATA PROTECTION</div>
</div>

<h2 class="section-title contact-title abs">CONTACT US</h2>
<div class="field f-name abs">Name</div>
<div class="field f-email abs">Email Id</div>
<div class="field f-message abs">Message</div>
<div class="send abs">
  <svg width="11" height="11" viewBox="0 0 12 12"><path d="M11 1 1 5.5l4 1.5 1.5 4z" fill="none" stroke="currentColor" stroke-width="1.2" stroke-linejoin="round"/><path d="M11 1 5 7" stroke="currentColor" stroke-width="1.2"/></svg>
  <span>Send</span>
</div>

<div class="footer-mark abs"></div>
<footer class="footer abs">
  <div class="f-item fi-1 abs">
    <span class="f-icon"><svg width="14" height="14" viewBox="0 0 14 14"><path d="M2 7 7 2.5 12 7M3.5 6v5.5h7V6" fill="none" stroke="#0f6fbf" stroke-width="1.6"/></svg></span>
    <div><div class="f-co">NORTHVALE LTD.</div>Lorem ipsum dummy text,<br>Country - 123456.</div>
  </div>
  <div class="f-item fi-2 abs">
    <span class="f-icon"><svg width="12" height="14" viewBox="0 0 12 14"><rect x="3" y="1" width="6" height="12" rx="1.2" fill="none" stroke="#0f6fbf" stroke-width="1.5"/><circle cx="6" cy="10.5" r=".8" fill="#0f6fbf"/></svg></span>
    <span>123 456 7890</span>
  </div>
  <div class="f-item fi-3 abs">
    <span class="f-icon"><svg width="14" height="12" viewBox="0 0 14 12"><rect x="1" y="2" width="12" height="8" rx="1" fill="#0f6fbf"/><path d="M1.5 2.8 7 7l5.5-4.2" fill="none" stroke="#fff" stroke-width="1.1"/></svg></span>
    <span>info@northvaleltd.com</span>
  </div>
  <div class="f-item fi-4 abs">
    <span class="f-icon"><svg width="14" height="14" viewBox="0 0 14 14"><circle cx="7" cy="7" r="5.3" fill="none" stroke="#0f6fbf" stroke-width="1.6"/><path d="M7 4v3.2h2.3" fill="none" stroke="#0f6fbf" stroke-width="1.4"/></svg></span>
    <div><b>MON - FRI :</b> 9 am to 5 pm<br><b>SAT - SUN :</b> Close</div>
  </div>
  <div class="rule abs"></div>
  <div class="copyright abs">© <b>NORTHVALE LTD.</b> - 2017. All rights reserved.</div>
</footer>

</body>
</html>
```